Modern Billboard Ad for Criminal Defense Firm

10.5 x 36 We're looking for something to set us apart from the local competition. Looking for sleek and modern. We're a mid-sized firm in a small market city. We want to give the artist room to be creative on this one.
Thanks

Target Market(s)

Adult clients who have been charged with a crime/DWI

Industry/Entity Type

legal

Font styles to use
Serif
Sans Serif

Requirements
Must have
• Needs to have the firm name in large lettering. Law Offices of Marcus T Whitfield. “PLLC” does not have to be included. Phone number of (555) 384-1927 should be included but not the main focus.
Nice to have
• A call to action or something similar. “Don’t go it alone, call today.”, “ Arrested?”

```html
<!DOCTYPE html>
<html lang="en">
<head>
<meta charset="utf-8">
<title>Law Offices of Marcus T Whitfield – Billboard</title>
<link rel="stylesheet" href="https://fonts.googleapis.com/css2?family=Noto+Sans:wght@700;800&display=swap">
<style>
  :root {
    --yellow: #fdbe16;
    --blue: #0096db;
    --ink: #1a1a1a;
    --white: #ffffff;
    --wood: #f1ebd2;
    --wood-edge: #ddd3ad;
    --photo-dark: #3a3a3a;
    --photo-light: #9a9a9a;
    --badge: #1c2a44;
    --backdrop: #e8ecf0;
  }
  * { margin: 0; padding: 0; box-sizing: border-box; }
  html, body {
    width: 1200px; height: 792px; overflow: hidden;
    background: var(--backdrop);
  }
  .billboard {
    position: absolute; left: 20px; top: 225px;
    width: 1160px; height: 342px;
    background: var(--yellow);
    font-family: "Noto Sans", Verdana, sans-serif;
    color: var(--ink);
    overflow: hidden;
  }
  .accent-column {
    position: absolute; left: 678px; top: 0; width: 112px; height: 342px;
    background: var(--blue);
  }
  .firm-name {
    position: absolute; left: 75px; top: 36px;
    font-size: 30px; font-weight: 800; letter-spacing: 0.4px;
    line-height: 1; white-space: nowrap;
  }
  .tagline {
    position: absolute; left: 147px;
    font-size: 52px; font-weight: 700; letter-spacing: 3px;
    line-height: 1; white-space: nowrap;
  }
  .tagline--first { top: 105px; }
  .tagline--second { top: 155px; }
  .phone-band {
    position: absolute; left: 0; top: 215px; width: 459px; height: 68px;
    background: var(--blue);
  }
  .phone {
    position: absolute; left: 75px; top: 224px;
    font-size: 47px; font-weight: 700; letter-spacing: 3px; line-height: 1;
    color: var(--white); white-space: nowrap;
  }
  .block {
    position: absolute;
    background: linear-gradient(180deg, var(--wood), var(--wood-edge));
    box-shadow: inset -1px 0 0 rgba(0,0,0,0.08);
  }
  .block svg { display: block; width: 100%; height: 100%; }
  .block--courthouse { left: 459px; top: 168px; width: 109px; height: 115px; }
  .block--scales { left: 569px; top: 168px; width: 109px; height: 115px; }
  .block--gavel { left: 678px; top: 133px; width: 112px; height: 114px; }
  .icon { fill: var(--ink); }
  .icon-line { stroke: var(--ink); fill: none; stroke-width: 2.5; }
  .portrait {
    position: absolute; left: 822px; top: 0; width: 338px; height: 342px;
    background: linear-gradient(135deg, var(--photo-light), var(--photo-dark));
  }
  .award-badge {
    position: absolute; left: 854px; top: 13px; width: 66px; height: 95px;
    background: var(--badge);
    border-bottom: 14px solid var(--blue);
  }
</style>
</head>
<body>
  <div class="billboard">
    <div class="accent-column"></div>
    <div class="firm-name">LAW OFFICES OF MARCUS T WHITFIELD</div>
    <div class="tagline tagline--first">Don’t go it alone</div>
    <div class="tagline tagline--second">Call today</div>
    <div class="phone-band"></div>
    <div class="phone">(555) 384-1927</div>

    <div class="block block--courthouse">
      <svg viewBox="0 0 109 115" role="img" aria-label="Courthouse icon">
        <polygon class="icon" points="57,24 96,50 19,50"/>
        <rect class="icon" x="22" y="52" width="72" height="6"/>
        <rect class="icon" x="26" y="60" width="9" height="22"/>
        <rect class="icon" x="42" y="60" width="9" height="22"/>
        <rect class="icon" x="58" y="60" width="9" height="22"/>
        <rect class="icon" x="74" y="60" width="9" height="22"/>
        <rect class="icon" x="19" y="83" width="78" height="9"/>
      </svg>
    </div>

    <div class="block block--scales">
      <svg viewBox="0 0 109 115" role="img" aria-label="Scales of justice icon">
        <circle class="icon-line" cx="53" cy="23" r="3.5"/>
        <rect class="icon" x="51" y="26" width="4" height="58"/>
        <rect class="icon" x="22" y="36" width="62" height="4"/>
        <line class="icon-line" x1="28" y1="40" x2="21" y2="62"/>
        <line class="icon-line" x1="28" y1="40" x2="35" y2="62"/>
        <line class="icon-line" x1="78" y1="40" x2="71" y2="62"/>
        <line class="icon-line" x1="78" y1="40" x2="85" y2="62"/>
        <path class="icon-line" d="M19 62 H37 A9 8 0 0 1 19 62 Z"/>
        <path class="icon-line" d="M69 62 H87 A9 8 0 0 1 69 62 Z"/>
        <polygon class="icon" points="45,84 61,84 66,92 40,92"/>
      </svg>
    </div>

    <div class="block block--gavel">
      <svg viewBox="0 0 112 114" role="img" aria-label="Gavel icon">
        <g transform="rotate(35 40 42)">
          <rect class="icon" x="22" y="34" width="36" height="18" rx="3"/>
          <rect class="icon" x="18" y="31" width="8" height="24" rx="3"/>
          <rect class="icon" x="54" y="31" width="8" height="24" rx="3"/>
        </g>
        <polygon class="icon" points="48,56 104,82 101,88 45,62"/>
        <circle class="icon" cx="101" cy="85" r="5"/>
        <rect class="icon" x="20" y="76" width="30" height="6" rx="2"/>
        <rect class="icon" x="15" y="83" width="40" height="7" rx="2"/>
      </svg>
    </div>

    <div class="portrait" role="img" aria-label="Black and white portrait of the attorney in a suit vest, jacket over his shoulder, against a wood wall"></div>
    <div class="award-badge" role="img" aria-label="Community award badge"></div>
  </div>
</body>
</html>
```